Self-Help Book Cover

This is a self-help book entitled, "Lanterns for Drifters, Oddballs & Dreamers: A grounded and soulful path toward finding where you belong on earth."
I want the book cover to be primarily white, with red and black as secondary colors. I am open to cartoon interpretations of the words, "misfits, weirdos, and introverts" or a unique font used for each word. For the center, there can be white/gray people/balls with larger red people/balls in the middle of them shaped like an antique key. Or the center can be a red door that opens to a pleasant background image (maybe nature). This is just some ideas, I am open to others.
The author's name is Marla Quenby. The text on the back of the book is in a word doc file attached. I have also attached samples of the key and people/balls.
Requirements
Must have
- a .jpg or .tif(f) file
- at least 1000 pixels on the longest side
- ideal image height/width ratio is 1.6 (example: 1000 x 1600)
- The size should be 5.5" x 8.5"

```html
<!DOCTYPE html>
<html lang="en">
<head>
<meta charset="utf-8">
<title>Lanterns for Drifters, Oddballs &amp; Dreamers — Cover Wrap</title>
<link rel="stylesheet" href="https://fonts.googleapis.com/css2?family=Questrial&family=Cabin:wght@500&family=Oswald:wght@500;700&family=Open+Sans:wght@800&display=swap">
<style>
  :root {
    --cover-red: #cf1f26;
    --cover-red-deep: #b8141c;
    --door-red: #e01d23;
    --door-red-dark: #a90f15;
    --ink: #0b0b0b;
    --paper: #ffffff;
    --title-gold-top: #fff14a;
    --title-gold-bottom: #f2a516;
    --subtitle-grey: #e9e9ee;
    --sky-top: #6f86c9;
    --sky-mid: #d874b8;
    --sky-warm: #f38a4a;
    --sky-low: #fcd23a;
    --sky-bottom: #fdeb8c;
  }
  * { box-sizing: border-box; margin: 0; padding: 0; }
  html, body { width: 1200px; height: 900px; overflow: hidden; background: var(--paper); }
  .cover-wrap { position: relative; width: 1200px; height: 900px; overflow: hidden; }

  .back-cover {
    position: absolute; left: 0; top: 0; width: 590px; height: 900px;
    background: linear-gradient(180deg, var(--cover-red) 0%, var(--cover-red-deep) 100%);
  }
  .back-blurb {
    position: absolute; left: 46px; top: 45px; width: 498px;
    font-family: "Questrial", sans-serif; font-size: 14.2px; line-height: 18.35px;
    color: var(--paper); text-align: justify; letter-spacing: 0.75px; word-spacing: 0.5px;
    -webkit-text-stroke: 0.35px var(--paper);
  }

  .spine {
    position: absolute; left: 588px; top: 0; width: 32px; height: 900px;
    background: linear-gradient(180deg, var(--cover-red) 0%, var(--cover-red-deep) 100%);
  }
  .spine svg { display: block; }
  .spine-title { font-family: "Oswald", sans-serif; font-weight: 500; font-size: 14px; fill: var(--paper); }

  .front-cover { position: absolute; left: 620px; top: 0; width: 580px; height: 900px; }
  .front-sky {
    position: absolute; inset: 0;
    background: linear-gradient(180deg, var(--sky-top) 0%, #9a86c8 18%, var(--sky-mid) 40%, var(--sky-warm) 62%, var(--sky-low) 82%, var(--sky-bottom) 100%);
  }
  .front-tagline {
    position: absolute; left: 40px; right: 20px; top: 16px;
    font-family: "Cabin", sans-serif; font-weight: 500; font-size: 25px; line-height: 34px;
    color: var(--paper); text-align: center; text-shadow: 0 1px 3px rgba(60, 40, 90, 0.45);
  }
  .front-title {
    position: absolute; left: 32px; right: 24px; top: 124px;
    font-family: "Oswald", sans-serif; font-weight: 700; font-size: 84px; line-height: 86px;
    text-align: center; letter-spacing: -1px;
    background: linear-gradient(180deg, var(--title-gold-top) 0%, var(--title-gold-bottom) 100%);
    -webkit-background-clip: text; background-clip: text; color: transparent;
  }
  .front-subtitle {
    position: absolute; left: 32px; right: 20px; top: 202px;
    font-family: "Cabin", sans-serif; font-weight: 500; font-size: 26px; letter-spacing: 3.2px;
    color: var(--subtitle-grey); text-align: center;
    text-shadow: 2px 2px 2px rgba(70, 40, 80, 0.6);
  }
  .door-art {
    position: absolute; left: 0; top: 258px; width: 338px; height: 642px;
    background: linear-gradient(100deg, var(--door-red-dark) 0%, var(--door-red) 45%, #e8434a 75%, var(--door-red) 100%);
  }
  .author-name {
    position: absolute; right: 14px; top: 724px;
    font-family: "Open Sans", sans-serif; font-weight: 800; font-size: 52px; line-height: 56px;
    color: var(--ink); text-align: center; letter-spacing: 0.5px;
  }
</style>
</head>
<body>
<main class="cover-wrap">
  <section class="back-cover">
    <p class="back-blurb">There are many self-help books out there for how to succeed, but I have found they all hold basic presumptions about the individuals reading them they assume the reader is a normal, everyday person. I would read books and would become disheartened because they didnt address the unique challenges I faced as a misfit. Conventional wisdom only partially helped me to overcome my specific hurdles. I grew up very poor without the resources or guidance that many of my peers had. I thought differently, dreamt differently, and most important, acted differently than those around me. Yet somehow I was able to have success in doing everything from being a military officer, a U.S. diplomat, an educator, and an entrepreneur. Perhaps the biggest lesson I have learned in my life is that when you are different, the rules are different as well. You are forced to think outside of the box because you dont fit into any. However, I have also learned that are misfits are divinely appointed by God to fulfill a specific purpose.<br>As a misfit, youve spent your entire life as a round peg trying to fit into a square hole. No one has ever spoken to your specific circumstance, or taught you how to exist in a world that doesnt get you. In our society, we are taught wear mask, blend in, and reject things we dont understand. Well what happens when you cant blend in? What happens when you are the thing that is misunderstood? We are constantly told to build up alter-egos, but we never have a chance to strip down and deal with the heart of who we are. Therefore, this is not a How to Charm Every Room You Enter book. In fact, this book is not about changing others reactions to you, but rather changing your reaction to others.<br>Your life will be different as a misfit, and how you prepare for that will determine if it is a good different or a bad different. Now is the time to use your unique attributes for your benefit, and to use them as a unique advantage. Misfits dont need cookie cutter advice, they need something that will meet them where they are, to get them to where they need to be. This book is designed to give you as many tools as possible to overcome whatever specific situation you are facing as a misfit, weirdo, or introvert. Because in the end, radically different people need radically different advice.</p>
  </section>

  <aside class="spine">
    <svg width="32" height="900" viewBox="0 0 32 900">
      <text class="spine-title" transform="translate(21 868) rotate(-90)" textLength="836" lengthAdjust="spacingAndGlyphs">LANTERNS FOR DRIFTERS, ODDBALLS &amp; DREAMERS: A GROUNDED AND SOULFUL PATH TOWARD FINDING WHERE YOU BELONG ON EARTH</text>
    </svg>
  </aside>

  <section class="front-cover">
    <div class="front-sky" role="img" aria-label="Sunset sky with clouds shifting from blue and violet to pink, orange and golden yellow"></div>
    <p class="front-tagline">A grounded and soulful path toward<br>finding where you belong on earth</p>
    <h1 class="front-title">LANTERNS FOR</h1>
    <h2 class="front-subtitle">DRIFTERS, ODDBALLS &amp; DREAMERS</h2>
    <div class="door-art" role="img" aria-label="Photograph of a red door in a red frame, swung open onto a glowing sunset sky"></div>
    <p class="author-name">MARLA<br>QUENBY</p>
  </section>
</main>
</body>
</html>
```